Waistline Ember Product Social Media Graphics

Focusing on the Waistline Ember product, create 5-6 individual social media graphics (square size). For the color scheme of the graphics, they should all be complementary with the Waistline Ember bottle colors.
Note: each graphic should have one of the 2 pictures of the bottle on it and/or one of the images with a person on it (several pics attached)/only use stock photography that I provided.
Target Market(s)
For men and women trying to lose belly fat
Industry/Entity Type
health and wellness
Look and feel
Each slider illustrates characteristics of the customer's brand and the style your logo design should communicate.

```html
<!DOCTYPE html>
<html lang="en">
<head>
<meta charset="utf-8">
<title>Waistline Ember – Social Media Graphics</title>
<link rel="stylesheet" href="https://fonts.googleapis.com/css2?family=Montserrat:wght@400;500;600;700;800&display=swap">
<style>
  :root{
    --ember:#e8402a;
    --ember-soft:rgba(232,64,42,.78);
    --blush:#fbe8e8;
    --mist:#d7d7d9;
    --sand:#e8d8b8;
    --white:#ffffff;
    --skin:#a86a4a;
    --skin-dark:#6f4330;
    --bottle:#f4f4f4;
  }
  *{box-sizing:border-box;margin:0;padding:0}
  html,body{width:1200px;height:560px;overflow:hidden}
  body{background:var(--sand);font-family:"Montserrat",sans-serif;position:relative}
  .panel{position:absolute;overflow:hidden;box-shadow:0 6px 8px rgba(0,0,0,.12)}
  .abs{position:absolute}
  .photo{position:absolute}
  .photo-body{background:linear-gradient(160deg,#e6e3e1 0%,#c99377 45%,var(--skin) 70%,#8aa6c4 100%)}
  .photo-portrait{background:linear-gradient(180deg,#e9e4de 0%,#b57a58 40%,var(--skin-dark) 75%,#d8d2cc 100%)}
  .photo-torso{background:linear-gradient(180deg,#f2f2f2 0%,#f2f2f2 25%,#b8795a 45%,var(--skin) 80%,#f1f1f1 100%)}
  .bottle{position:absolute;border-radius:10px;background:linear-gradient(90deg,#dcdcdc,var(--bottle) 40%,#ffffff 60%,#d9d9d9)}
  .bottle::after{content:"";position:absolute;left:0;right:0;bottom:18%;height:16%;background:var(--ember);opacity:.85}
  .dots{position:absolute;display:grid;gap:3px}
  .dots i{display:block;width:4px;height:4px;border-radius:50%;background:var(--ember)}
  .dots.light i{background:var(--white)}
  .vertical{position:absolute;writing-mode:vertical-rl;transform:rotate(180deg);font-weight:700;white-space:nowrap}
  .white{color:var(--white)}
  .red{color:var(--ember)}
  .h{font-weight:800;line-height:1.02}
  .body-copy{font-weight:400;line-height:1.25}

  /* Large feature square */
  .feature{left:70px;top:66px;width:430px;height:428px;background:var(--mist)}
  .feature .left-col{left:0;top:0;width:182px;height:428px;background:var(--mist)}
  .feature .arch{left:15px;top:0;width:68px;height:63px;background:var(--blush);border-radius:0 0 34px 34px}
  .feature .bloat-band{left:0;top:78px;width:182px;height:62px;background:var(--ember);padding:10px 0 0 19px}
  .feature .strip{left:182px;top:0;width:90px;height:428px;background:var(--blush)}
  .feature .right-photo{left:272px;top:0;width:158px;height:392px}
  .feature .tummy-band{left:272px;top:140px;width:158px;height:50px;background:var(--ember-soft);display:flex;align-items:center;justify-content:center}
  .feature .foot{top:392px;height:36px;background:var(--ember);display:flex;align-items:center;justify-content:center;color:var(--white);font-weight:700;font-size:20px;letter-spacing:1px}
</style>
</head>
<body>

<!-- Feature square -->
<section class="panel feature">
  <div class="abs left-col"></div>
  <div class="abs arch"></div>
  <div class="abs bloat-band">
    <p class="white" style="font-weight:700;font-size:14px;letter-spacing:.5px">BELLY BLOAT</p>
    <p class="white h" style="font-size:27px">NO MORE</p>
  </div>
  <p class="abs red" style="left:19px;top:154px;width:160px;font-weight:700;font-size:11px;line-height:1.3;letter-spacing:.3px">DISCOVER THE SECRET TO A FLATTER TUMM</p>
  <div class="dots" style="left:23px;top:204px;grid-template-columns:repeat(2,4px);gap:6px 4px">
    <i></i><i></i><i></i><i></i><i></i><i></i><i></i><i></i><i></i><i></i><i></i><i></i>
  </div>
  <p class="abs red" style="left:19px;top:283px;width:70px;font-size:10.5px;line-height:1.18;font-weight:400">consectet ur adipiscing elit. Ut enim elit, luctus quis imperdiet id, rutrum</p>
  <div class="abs strip"></div>
  <div class="photo photo-body right-photo" role="img" aria-label="Photo of a slim torso in a white sports top and loose jeans"></div>
  <div class="dots" style="left:286px;top:18px;grid-template-columns:repeat(6,5px);gap:6px 5px">
    <i style="width:5px;height:5px"></i><i style="width:5px;height:5px"></i><i style="width:5px;height:5px"></i><i style="width:5px;height:5px"></i><i style="width:5px;height:5px"></i><i style="width:5px;height:5px"></i>
    <i style="width:5px;height:5px"></i><i style="width:5px;height:5px"></i><i style="width:5px;height:5px"></i><i style="width:5px;height:5px"></i><i style="width:5px;height:5px"></i><i style="width:5px;height:5px"></i>
  </div>
  <div class="abs tummy-band"><p class="white" style="font-weight:700;font-size:15px;letter-spacing:.5px">FLATTER TUMMY</p></div>
  <div class="abs foot" style="left:0;width:182px">&gt;&gt;&gt;&gt;&gt;</div>
  <div class="abs" style="left:182px;top:392px;width:90px;height:36px;background:var(--blush)"></div>
  <div class="abs foot" style="left:272px;width:158px">&gt;&gt;&gt;&gt;&gt;</div>
  <div class="bottle" role="img" aria-label="Product bottle of Waistline Ember capsules" style="left:168px;top:235px;width:120px;height:170px;transform:rotate(32deg);border-radius:18px"></div>
  <p class="vertical red" style="left:205px;top:48px;font-size:34px;letter-spacing:1px">WAISTLINE EMBER</p>
</section>

<!-- Small 1 -->
<section class="panel" style="left:525px;top:65px;width:198px;height:198px">
  <div class="photo photo-portrait" style="left:0;top:0;width:198px;height:198px" role="img" aria-label="Photo of a smiling woman holding out oversized jeans"></div>
  <div class="abs" style="left:12px;top:0;width:31px;height:28px;background:var(--ember);border-radius:0 0 16px 16px"></div>
  <div class="abs" style="left:125px;top:0;width:73px;height:64px;background:var(--ember);border-radius:0 0 0 64px"></div>
  <p class="abs white" style="left:140px;top:8px;width:56px;font-weight:700;font-size:10px;line-height:1.2;text-align:center">WAISTLINE EMBER</p>
  <div class="dots" style="left:18px;top:43px;grid-template-columns:repeat(6,3px);gap:2px">
    <i style="width:3px;height:3px"></i><i style="width:3px;height:3px"></i><i style="width:3px;height:3px"></i><i style="width:3px;height:3px"></i><i style="width:3px;height:3px"></i><i style="width:3px;height:3px"></i>
    <i style="width:3px;height:3px"></i><i style="width:3px;height:3px"></i><i style="width:3px;height:3px"></i><i style="width:3px;height:3px"></i><i style="width:3px;height:3px"></i><i style="width:3px;height:3px"></i>
  </div>
  <div class="abs" style="left:0;top:77px;width:198px;height:56px;background:var(--ember-soft);padding:7px 10px 0;text-align:center">
    <p class="white h" style="font-size:12.5px">REDUCE BELLY FAT AND BLOATING OVERNIGHT</p>
    <p class="white body-copy" style="font-size:5px;margin-top:4px">A gentle daily blend that supports digestion and helps you feel lighter.</p>
  </div>
  <div class="bottle" style="left:6px;top:140px;width:18px;height:40px;border-radius:4px" role="img" aria-label="Product bottle"></div>
  <div class="bottle" style="left:24px;top:138px;width:20px;height:42px;border-radius:4px" role="img" aria-label="Product bottle"></div>
  <div class="bottle" style="left:44px;top:140px;width:18px;height:40px;border-radius:4px" role="img" aria-label="Product bottle"></div>
  <p class="abs red" style="right:8px;top:164px;font-weight:700;font-size:6px;text-align:right;line-height:1.2">Reduced<br>bloating</p>
  <div class="abs" style="left:0;top:181px;width:198px;height:17px;background:var(--ember)"></div>
</section>

<!-- Small 2 -->
<section class="panel" style="left:731px;top:65px;width:198px;height:198px;background:var(--blush)">
  <div class="photo photo-body" style="left:0;top:0;width:198px;height:198px" role="img" aria-label="Photo of hands forming a heart over a bare stomach"></div>
  <div class="abs" style="left:0;top:0;width:115px;height:27px;background:var(--ember)"></div>
  <div class="abs" style="left:155px;top:0;width:32px;height:27px;background:var(--ember);border-radius:0 0 16px 16px"></div>
  <div class="dots light" style="left:10px;top:10px;grid-template-columns:repeat(6,3px);gap:2px">
    <i style="width:3px;height:3px"></i><i style="width:3px;height:3px"></i><i style="width:3px;height:3px"></i><i style="width:3px;height:3px"></i><i style="width:3px;height:3px"></i><i style="width:3px;height:3px"></i>
    <i style="width:3px;height:3px"></i><i style="width:3px;height:3px"></i><i style="width:3px;height:3px"></i><i style="width:3px;height:3px"></i><i style="width:3px;height:3px"></i><i style="width:3px;height:3px"></i>
  </div>
  <div class="abs" style="left:0;top:27px;width:198px;height:41px;background:var(--blush);padding:9px 0 0 10px">
    <p class="red h" style="font-size:17.5px">WAISTLINE EMBER</p>
  </div>
  <div class="abs" style="left:0;top:68px;width:112px;height:172px;background:var(--ember);border-radius:0 0 90px 0"></div>
  <div class="abs" style="left:10px;top:76px;width:100px">
    <p class="white h" style="font-size:10.5px">REDUCE<br>BELLY FAT FAST</p>
    <p class="white" style="font-weight:600;font-size:6px;margin-top:7px;line-height:1.3">THE GUT CLEANSE YOU<br>NEED TO TRY</p>
    <p class="white body-copy" style="font-size:5px;margin-top:7px;width:62px">A daily blend for a calmer gut and lighter feel.</p>
  </div>
  <div class="bottle" style="left:88px;top:126px;width:28px;height:50px;transform:rotate(-28deg);border-radius:5px" role="img" aria-label="Product bottle"></div>
  <div class="abs" style="left:132px;top:178px;width:66px;height:20px;background:var(--ember);display:flex;align-items:center;justify-content:center">
    <p class="white" style="font-weight:700;font-size:6px">Improved digestion</p>
  </div>
</section>

<!-- Small 3 -->
<section class="panel" style="left:936px;top:65px;width:198px;height:198px;background:var(--ember)">
  <div class="photo photo-torso" style="left:125px;top:0;width:73px;height:198px" role="img" aria-label="Photo of a slim waist with a measuring tape"></div>
  <div class="abs" style="left:0;top:0;width:140px;height:110px;background:var(--ember);border-radius:0 0 60px 0"></div>
  <div class="abs" style="left:10px;top:14px;width:125px">
    <p class="white" style="font-weight:700;font-size:6.5px">WANT A FLATTER STOMACH?</p>
    <p class="white h" style="font-size:12.5px;margin-top:2px">THIS GUT<br>CLEANSE COULD<br>BE THE KEY</p>
  </div>
  <div class="dots light" style="left:10px;top:78px;grid-template-columns:repeat(6,3px);gap:2px">
    <i style="width:3px;height:3px"></i><i style="width:3px;height:3px"></i><i style="width:3px;height:3px"></i><i style="width:3px;height:3px"></i><i style="width:3px;height:3px"></i><i style="width:3px;height:3px"></i>
    <i style="width:3px;height:3px"></i><i style="width:3px;height:3px"></i><i style="width:3px;height:3px"></i><i style="width:3px;height:3px"></i><i style="width:3px;height:3px"></i><i style="width:3px;height:3px"></i>
  </div>
  <div class="abs" style="left:134px;top:102px;width:64px;height:18px;background:var(--ember-soft);display:flex;align-items:center;justify-content:center">
    <p class="white" style="font-weight:600;font-size:6px">Increased energy</p>
  </div>
  <div class="abs" style="left:118px;top:140px;width:80px;height:58px;background:var(--ember);border-radius:60px 0 0 0"></div>
  <p class="abs white" style="left:138px;top:168px;width:60px;font-weight:700;font-size:10px;line-height:1.05;text-align:center">WAISTLINE EMBER</p>
  <div class="bottle" style="left:14px;top:110px;width:36px;height:78px;border-radius:6px" role="img" aria-label="Product bottle"></div>
  <div class="bottle" style="left:46px;top:104px;width:40px;height:86px;border-radius:6px" role="img" aria-label="Product bottle"></div>
  <div class="bottle" style="left:84px;top:110px;width:36px;height:78px;border-radius:6px" role="img" aria-label="Product bottle"></div>
</section>

<!-- Small 4 -->
<section class="panel" style="left:525px;top:296px;width:198px;height:198px;background:var(--ember)">
  <div class="photo photo-torso" style="left:0;top:0;width:90px;height:198px" role="img" aria-label="Photo of a woman's toned midriff in a white top"></div>
  <div class="abs" style="left:0;top:0;width:44px;height:28px;background:var(--ember-soft);border-radius:0 0 20px 0"></div>
  <div class="abs" style="left:0;top:154px;width:83px;height:44px;background:var(--ember);border-radius:14px 14px 0 0"></div>
  <div class="abs" style="left:83px;top:0;width:24px;height:198px;background:var(--blush);border-radius:12px 0 0 12px"></div>
  <p class="vertical red" style="left:88px;top:34px;font-size:11px">WAISTLINE EMBER</p>
  <div class="abs" style="left:112px;top:13px;width:82px">
    <p class="white" style="font-weight:700;font-size:8px">GET RID OF TOXINS</p>
    <p class="white" style="font-weight:600;font-size:4.5px;margin-top:2px">TO REVEAL A FLATTER TUMMY</p>
    <p class="white" style="font-weight:600;font-size:4.5px;margin-top:9px">Lorem ipsum dolor sit amet,</p>
    <p class="white body-copy" style="font-size:4.5px;margin-top:6px;width:72px">Natural fibres and botanicals help sweep away waste and support regular digestion.</p>
  </div>
  <div class="abs" style="left:107px;top:93px;width:91px;height:86px;background:var(--ember)"></div>
  <div class="dots light" style="left:160px;top:98px;grid-template-columns:repeat(6,3px);gap:2px">
    <i style="width:3px;height:3px"></i><i style="width:3px;height:3px"></i><i style="width:3px;height:3px"></i><i style="width:3px;height:3px"></i><i style="width:3px;height:3px"></i><i style="width:3px;height:3px"></i>
    <i style="width:3px;height:3px"></i><i style="width:3px;height:3px"></i><i style="width:3px;height:3px"></i><i style="width:3px;height:3px"></i><i style="width:3px;height:3px"></i><i style="width:3px;height:3px"></i>
  </div>
  <div class="bottle" style="left:128px;top:100px;width:42px;height:72px;transform:rotate(-30deg);border-radius:7px" role="img" aria-label="Product bottle"></div>
  <p class="abs white" style="left:107px;top:184px;width:91px;font-weight:700;font-size:7.5px;text-align:center">FLATTER TUMMY</p>
</section>

<!-- Small 5 -->
<section class="panel" style="left:731px;top:296px;width:198px;height:198px;background:var(--blush)">
  <div class="photo photo-torso" style="left:0;top:0;width:198px;height:176px" role="img" aria-label="Photo of a woman in white underwear showing a flat stomach"></div>
  <p class="vertical white" style="left:8px;top:8px;font-size:17px;opacity:.85">WAISTLINE EMBER</p>
  <div class="abs" style="left:70px;top:0;width:128px;height:176px;background:var(--ember);border-radius:28px 0 0 0"></div>
  <div class="abs" style="right:8px;top:10px;width:118px;text-align:right">
    <p class="white h" style="font-size:10px">HEALTHY STOMACH</p>
    <p class="white" style="font-weight:600;font-size:7px;margin-top:1px">FOR A SEXIER APPEARANCE</p>
    <p class="white" style="font-weight:600;font-size:4.5px;margin-top:7px">Lorem ipsum dolor sit amet,</p>
    <p class="white body-copy" style="font-size:4.5px;margin-top:5px">Plant based ingredients support a balanced gut, steady digestion and a calmer, flatter stomach every day.</p>
  </div>
  <div class="abs" style="left:112px;top:86px;width:86px;height:16px;background:var(--blush);display:flex;align-items:center;justify-content:flex-end;padding-right:12px">
    <p class="red" style="font-weight:700;font-size:7px">Flatter Tummy</p>
  </div>
  <div class="dots light" style="left:160px;top:116px;grid-template-columns:repeat(6,3px);gap:2px">
    <i style="width:3px;height:3px"></i><i style="width:3px;height:3px"></i><i style="width:3px;height:3px"></i><i style="width:3px;height:3px"></i><i style="width:3px;height:3px"></i><i style="width:3px;height:3px"></i>
    <i style="width:3px;height:3px"></i><i style="width:3px;height:3px"></i><i style="width:3px;height:3px"></i><i style="width:3px;height:3px"></i><i style="width:3px;height:3px"></i><i style="width:3px;height:3px"></i>
  </div>
  <p class="abs white body-copy" style="right:10px;top:135px;width:84px;font-size:4.5px;text-align:right">Two capsules a day with water help keep bloating away.</p>
  <div class="bottle" style="left:70px;top:70px;width:44px;height:76px;transform:rotate(30deg);border-radius:7px" role="img" aria-label="Product bottle"></div>
</section>

<!-- Small 6 -->
<section class="panel" style="left:937px;top:296px;width:198px;height:198px;background:var(--blush)">
  <div class="photo photo-portrait" style="left:0;top:0;width:105px;height:198px" role="img" aria-label="Photo of a smiling woman with braids pulling at a loose waistband"></div>
  <div class="dots" style="left:12px;top:14px;grid-template-columns:4px;gap:2px">
    <i style="width:3px;height:3px"></i><i style="width:3px;height:3px"></i><i style="width:3px;height:3px"></i><i style="width:3px;height:3px"></i><i style="width:3px;height:3px"></i><i style="width:3px;height:3px"></i>
  </div>
  <div class="abs" style="left:158px;top:0;width:30px;height:28px;background:var(--ember);border-radius:0 0 16px 16px"></div>
  <div class="dots" style="left:88px;top:14px;grid-template-columns:repeat(6,3px);gap:2px">
    <i style="width:3px;height:3px"></i><i style="width:3px;height:3px"></i><i style="width:3px;height:3px"></i><i style="width:3px;height:3px"></i><i style="width:3px;height:3px"></i><i style="width:3px;height:3px"></i>
  </div>
  <div class="abs" style="left:86px;top:36px;width:110px">
    <p class="red" style="font-weight:600;font-size:8px">WAISTLINE EMBER</p>
    <p class="red h" style="font-size:19px;margin-top:2px">BELLY FAT</p>
    <p class="red" style="font-weight:500;font-size:6px;margin-top:2px">DISAPPEARSBODY BECOMES</p>
    <p class="red h" style="font-size:20px;margin-top:4px">IDEAL</p>
  </div>
  <div class="abs" style="left:60px;top:102px;width:138px;height:16px;background:var(--ember);display:flex;align-items:center;justify-content:flex-end;padding-right:9px">
    <p class="white" style="font-weight:700;font-size:7px">FLATTER TUMMY</p>
  </div>
  <div class="abs" style="left:70px;top:118px;width:128px;height:80px;background:var(--ember);opacity:.85;border-radius:70px 0 0 0"></div>
  <p class="abs white body-copy" style="right:10px;top:145px;width:56px;font-size:4.5px;text-align:right">Support your goals with a simple daily gut cleanse made from natural ingredients.</p>
  <div class="bottle" style="left:56px;top:136px;width:20px;height:46px;border-radius:4px" role="img" aria-label="Product bottle"></div>
  <div class="bottle" style="left:76px;top:132px;width:22px;height:50px;border-radius:4px" role="img" aria-label="Product bottle"></div>
  <div class="bottle" style="left:98px;top:136px;width:20px;height:46px;border-radius:4px" role="img" aria-label="Product bottle"></div>
</section>

</body>
</html>
```